Zielgruppe
Wir produzieren Nudeln.
Zielgruppe sind Einheimische und Touristen, 1.die den Unterschied zur Industrieware schätzen und gute Produkte sich selbst gönnen
2. die ein Geschenk oder Genuss aus dem Allgäu mitnehmen möchten
Aufgabenstellung
Produktetikett für Nudeln.
Es soll den Kunden davon überzeugen, genau dieses Nudelpaket aus dem Regal zu kaufen. Es soll suggerieren dass es sich um sehr gute Qualität handelt die man schmeckt.
Es soll im Regal auffallen um sich die Nudeln auch als Geschenk mitzunehmen.
Es soll die Region Allgäu, Westallgäu mit Adelegg wiederspiegeln.
Die Abmessung beträgt Breite 10cm Höhe 12cm, jeweils plus 3mm Beschnittzugabe für die Druckerei.
Es gibt nur eine Vorderseite.
Es soll nicht verspielt wirken. Gern mit Witz.
Slogan zum Beispiel: Kettlers Spätzla-echte Allgäuer Pasta. Hier kann gern auch ein anderer passender Slogan verwendet werden.
Das Etikett sollte auf verschiedene Themenbereiche anwendbar sein, da wir unterschiedliche Nudelsorten produzieren.
Verkaufsorte sind kleine Dorfläden, Laden in Manufaktur, wo auch andere Erzeuger ihre selbstgemachten Produkte für Einheimische und Touristen anbieten. Lebensmittelautomaten und Direktverkauf.

```html
<!DOCTYPE html>
<html lang="de">
<head>
<meta charset="utf-8">
<title>Kettlers Spätzla – Spaghetti Etikett</title>
<link rel="stylesheet" href="https://fonts.googleapis.com/css2?family=Playfair+Display:wght@400&family=Montserrat:wght@600&family=Source+Sans+3:wght@400&display=swap">
<style>
  :root {
    --paper: #f7f7f7;
    --ink: #1d1d33;
    --text: #1a1a1a;
    --cream: #f1eee7;
    --white: #ffffff;
    --rule: #b9b9b9;
    --sketch-light: #eeeeee;
    --sketch-dark: #c9c9cc;
  }
  * { margin: 0; padding: 0; box-sizing: border-box; }
  html, body { width: 848px; height: 1200px; overflow: hidden; background: var(--paper); }
  .label { position: relative; width: 848px; height: 1200px; background: var(--paper); color: var(--text); font-family: "Source Sans 3", Arial, sans-serif; }

  .hero-scene {
    position: absolute; left: 97px; top: 55px; width: 658px; height: 300px;
    background: radial-gradient(ellipse at 50% 60%, var(--sketch-dark) 0%, var(--sketch-light) 60%, var(--paper) 100%);
    border-radius: 50% 50% 8px 8px / 70% 70% 8px 8px;
  }

  .rule { position: absolute; left: 81px; width: 682px; height: 2px; background: var(--ink); }
  .rule--top { top: 374px; }
  .rule--bottom { top: 551px; }

  .brand-name {
    position: absolute; left: 81px; width: 682px; top: 376px; height: 175px;
    display: flex; align-items: center; justify-content: center;
    font-family: "Source Sans 3", Arial, sans-serif; font-weight: 400; font-size: 76px; color: var(--ink); line-height: 1;
  }

  .slogan {
    position: absolute; left: 0; width: 848px; top: 585px; text-align: center;
    font-family: "Playfair Display", Georgia, serif; font-size: 29px; line-height: 34px; color: var(--text);
  }

  .variety-band {
    position: absolute; left: 81px; top: 680px; width: 682px; height: 87px; background: var(--ink);
    display: flex; align-items: center; justify-content: center;
  }
  .variety-name { font-family: "Montserrat", Arial, sans-serif; font-weight: 600; font-size: 52px; color: var(--white); letter-spacing: 1px; line-height: 1; padding-bottom: 8px; }

  .info-box { position: absolute; padding: 12px 14px; font-size: 16px; line-height: 22px; font-style: normal; }
  .info-box--cream { background: var(--cream); }
  .info-box--white { background: var(--white); }
  .info-box__title { font-family: "Playfair Display", Georgia, serif; font-size: 18px; line-height: 22px; }
  .maker { left: 81px; top: 829px; width: 167px; height: 110px; padding-left: 17px; }
  .cook-time { left: 270px; top: 827px; width: 169px; height: 112px; padding-top: 13px; }
  .best-before { left: 81px; top: 961px; width: 169px; height: 113px; padding-left: 15px; }
  .ingredients { left: 271px; top: 959px; width: 168px; height: 115px; }

  .nutrition {
    position: absolute; left: 474px; top: 827px; width: 289px;
    border: 1px solid var(--rule); border-collapse: collapse; background: var(--white); font-size: 16px;
  }
  .nutrition caption { display: none; }
  .nutrition th { background: var(--cream); font-weight: 400; text-align: center; line-height: 23px; padding: 1px 4px 2px; height: 47px; }
  .nutrition td { border-top: 1px solid var(--rule); padding: 3px 7px; height: 29px; line-height: 22px; vertical-align: top; }
  .nutrition td.value { text-align: right; white-space: nowrap; padding-right: 3px; }
  .nutrition tr.tall td { height: 53px; }

  .net-weight {
    position: absolute; left: 97px; top: 1098px;
    font-family: "Playfair Display", Georgia, serif; font-size: 62px; line-height: 1; color: #000;
  }
</style>
</head>
<body>
<main class="label">
  <div class="hero-scene" role="img" aria-label="Gezeichnete Allgäuer Berglandschaft mit Tannen und Holzhütte"></div>

  <div class="rule rule--top"></div>
  <h1 class="brand-name">Kettlers Spätzla</h1>
  <div class="rule rule--bottom"></div>

  <p class="slogan">Von der Adelegg auf den Teller –<br>Handgemacht, wie’s sich g’hört!</p>

  <div class="variety-band"><span class="variety-name">spaghetti</span></div>

  <address class="info-box info-box--cream maker">
    <div class="info-box__title">Kettlers Spätzla</div>
    Am Rain 4<br>88400<br>Talweiler
  </address>

  <div class="info-box info-box--white cook-time">
    <div class="info-box__title">Kochzeit</div>
    AL DENTE KOCHEN NICHT NACH DER UHR
  </div>

  <div class="info-box info-box--white best-before">Mindestens haltbar bis:</div>

  <div class="info-box info-box--cream ingredients">
    <div class="info-box__title">Zutaten:</div>
    Hartweizengrieß
  </div>

  <table class="nutrition">
    <caption>Nährwerte</caption>
    <tr><th colspan="2">Durchschnittliche Nährwerte<br>(ungekocht, pro 100 g):</th></tr>
    <tr><td>Brennwert:</td><td class="value">1569 kJ / 370 kcal</td></tr>
    <tr><td>Fett:</td><td class="value">2,6 g</td></tr>
    <tr class="tall"><td>davon gesättigte<br>Fettsäuren:</td><td class="value">0,6 g</td></tr>
    <tr><td>Kohlenhydrate:</td><td class="value">71 g</td></tr>
    <tr><td>davon Zucker:</td><td class="value">3,3 g</td></tr>
    <tr><td>Eiweiß:</td><td class="value">14 g</td></tr>
    <tr><td>Salz:</td><td class="value">0,05 g</td></tr>
  </table>

  <div class="net-weight">500 g</div>
</main>
</body>
</html>
```